We are a specialised ICT Consultancy firm based in Perth, Western Australia. We are looking for an A4 brochure titled “Building Tomorrow Together” that we can use. I have created the content we would like for the brochure in the attachment “Building Tomorrow Together.docx”.
We would like the following on the brochure:
• A copy of the Australian Flag (can be static or rippling in the wind).
• Our logo
• Must be the Northvale blue theme
I have included copies of similar brochures so the designer can get an idea of the theme we are looking for.

```html
<!DOCTYPE html>
<html lang="en">
<head>
<meta charset="utf-8">
<title>Building Tomorrow Together – Brochure Spread</title>
<link href="https://fonts.googleapis.com/css2?family=Archivo:wdth,wght@125,800&family=Inter:wght@400;500&display=swap" rel="stylesheet">
<style>
  :root {
    --backdrop: #cdcdcd;
    --navy-deep: #2e3a4f;
    --navy: #3e4b62;
    --slate: #62718a;
    --paper-light: #e9e9ea;
    --paper-mid: #c4c6ca;
    --brand-blue: #1f80d8;
    --glow: #7cc4ff;
    --white: #ffffff;
    --text-soft: #dfe5ee;
  }
  * { margin: 0; padding: 0; box-sizing: border-box; }
  html, body { width: 1200px; height: 900px; overflow: hidden; }
  body { background: var(--backdrop); position: relative; font-family: "Inter", sans-serif; }

  .spread {
    position: absolute; left: 180px; top: 153px;
    width: 840px; height: 594px; display: flex;
    box-shadow: 0 18px 40px rgba(0,0,0,.25);
  }
  .page { position: relative; width: 420px; height: 594px; overflow: hidden; }

  /* Inside page */
  .page--inside {
    background: radial-gradient(circle at 80% 18%, var(--slate) 0%, var(--navy) 45%, var(--navy-deep) 100%);
  }
  .section-title {
    position: absolute; left: 34px; top: 42px; width: 230px;
    font-family: "Archivo", sans-serif; font-stretch: 125%; font-weight: 800;
    font-size: 22px; line-height: 1.05; color: var(--white); text-transform: uppercase;
  }
  .section-body {
    position: absolute; left: 34px; top: 124px; width: 300px;
    font-size: 9.2px; line-height: 1.45; color: var(--text-soft);
  }
  .cycle-diagram { position: absolute; left: 20px; top: 280px; width: 300px; height: 300px; }
  .cycle-label {
    font-family: "Archivo", sans-serif; font-stretch: 125%; font-weight: 800;
    font-size: 15px; fill: var(--white);
  }

  /* Cover page */
  .page--cover {
    background: radial-gradient(circle at 75% 40%, var(--slate) 0%, var(--navy) 50%, var(--navy-deep) 100%);
  }
  .cover-corner { position: absolute; left: 0; top: 0; width: 420px; height: 200px; }
  .brand {
    position: absolute; left: 150px; top: 70px;
    display: flex; align-items: center; gap: 10px;
  }
  .brand-mark { width: 22px; height: 22px; background: var(--navy); }
  .brand-name {
    font-family: "Inter", sans-serif; font-weight: 500; font-size: 15px;
    letter-spacing: .08em; color: var(--navy); text-transform: uppercase;
  }
  .flag-area {
    position: absolute; left: -60px; top: 440px; width: 340px; height: 200px;
    background: radial-gradient(closest-side, rgba(150,40,60,.55) 0%, rgba(28,47,102,.75) 45%, rgba(28,47,102,.35) 75%, rgba(46,58,79,0) 100%);
    z-index: 0;
  }
  .cover-title {
    position: absolute; left: 100px; top: 262px; width: 300px; text-align: center; z-index: 1;
    font-family: "Archivo", sans-serif; font-stretch: 125%; font-weight: 800;
    font-size: 34px; line-height: .98; text-transform: uppercase; color: var(--white);
  }
  .cover-title .accent { color: var(--brand-blue); display: block; }
  .cover-intro {
    position: absolute; left: 100px; top: 382px; width: 300px; text-align: center; z-index: 1;
    font-size: 9.2px; line-height: 1.45; color: var(--text-soft);
  }
</style>
</head>
<body>
  <main class="spread">
    <section class="page page--inside">
      <h2 class="section-title">The Challenge of Big Tech Tax Avoidance</h2>
      <p class="section-body">Multinational IT corporations frequently minimise their Australian tax obligations by artificially inflating costs to local subsidiaries. This shifts profits offshore and drastically reduces domestic margins, allowing them to avoid paying their fair share of Australian tax. As a local provider, Northvale ensures your ICT spending actively contributes to the Australian tax base and supports national growth.</p>

      <svg class="cycle-diagram" viewBox="0 0 300 300" aria-label="Tax avoidance cycle diagram">
        <defs>
          <filter id="ring-glow" x="-20%" y="-20%" width="140%" height="140%">
            <feGaussianBlur stdDeviation="3" result="b"/>
            <feMerge><feMergeNode in="b"/><feMergeNode in="SourceGraphic"/></feMerge>
          </filter>
        </defs>
        <g fill="none" stroke="var(--glow)" stroke-width="2" filter="url(#ring-glow)">
          <circle cx="150" cy="150" r="130"/>
          <circle cx="150" cy="150" r="78"/>
        </g>
        <text class="cycle-label" x="150" y="146" text-anchor="middle">TAX</text>
        <text class="cycle-label" x="150" y="166" text-anchor="middle">AVOIDANCE</text>
        <g transform="translate(175,22)" fill="none" stroke="var(--white)" stroke-width="2">
          <rect x="0" y="0" width="30" height="38" rx="2" fill="var(--navy)"/>
          <line x1="6" y1="14" x2="24" y2="14"/><line x1="6" y1="21" x2="24" y2="21"/><line x1="6" y1="28" x2="18" y2="28"/>
          <text x="15" y="10" text-anchor="middle" font-size="7" fill="var(--white)" stroke="none" font-family="Inter, sans-serif">TAX</text>
        </g>
        <g transform="translate(34,105)">
          <circle cx="16" cy="16" r="16" fill="var(--white)"/>
          <circle cx="16" cy="16" r="6" fill="var(--navy)"/>
        </g>
        <g fill="none" stroke="var(--white)" stroke-width="2">
          <path d="M240 170 c-8 0 -12 6 -12 11 c0 7 12 18 12 18 s12 -11 12 -18 c0 -5 -4 -11 -12 -11z"/>
          <circle cx="240" cy="181" r="3.5"/>
          <path d="M266 205 c-7 0 -10 5 -10 9 c0 6 10 15 10 15 s10 -9 10 -15 c0 -4 -3 -9 -10 -9z"/>
          <path d="M240 205 q-8 14 6 20 t14 10" stroke-dasharray="3 3"/>
        </g>
        <g transform="translate(95,248)" fill="none" stroke="var(--white)" stroke-width="2">
          <rect x="0" y="8" width="40" height="28" rx="3" fill="var(--navy)"/>
          <path d="M13 8 v-6 h14 v6"/><line x1="0" y1="20" x2="40" y2="20"/>
          <rect x="17" y="16" width="6" height="8"/>
        </g>
      </svg>
    </section>

    <section class="page page--cover">
      <svg class="cover-corner" viewBox="0 0 420 200" aria-hidden="true">
        <defs>
          <linearGradient id="corner-paper" x1="0" y1="0" x2="1" y2="1">
            <stop offset="0" stop-color="var(--paper-mid)"/>
            <stop offset=".5" stop-color="var(--paper-light)"/>
            <stop offset="1" stop-color="var(--paper-mid)"/>
          </linearGradient>
        </defs>
        <path d="M0 0 H420 V120 C300 160 180 185 0 185 Z" fill="url(#corner-paper)"/>
      </svg>
      <div class="brand">
        <span class="brand-mark"></span>
        <span class="brand-name">Northvale</span>
      </div>

      <div class="flag-area" role="img" aria-label="Australian flag rippling in the wind"></div>

      <h1 class="cover-title">Building <span class="accent">Tomorrow</span> Together</h1>
      <p class="cover-intro">As a 100% Western Australian-owned ICT provider, Northvale Technologies delivers top-tier tech solutions with a commitment to ethical sourcing that puts Australia first. By partnering with Northvale, you are keeping your investment local and supporting Australia's future.</p>
    </section>
  </main>
</body>
</html>
```